Website for a financial survey consultancy

WHO WE ARE
We're a niche HR consultancy specialising in salary comparison surveys for the financial asset management industry. We position ourselves as a small, highly responsive organisation with a strong personal relationship with each of our 50+ blue-chip clients.

WHAT WE DO
Our business is 80% surveys (= products), 20% consultancy (= services). The surveys are a set of online products which clients interact with to find the information they are interested in.

WHAT WE WANT
We are completely revising our existing marketing website and need a new up-to-date look and feel for the site. We want you to design 2 web pages
- Home page
- Internal content page

More details below in Must Have Priorities.

REFERENCE SITES
- www.tallowmere.com - nice background image
- www.quimbelt.com - ignoring the animations
- www.palvastro.com
- www.dulmiko.com - clean, fresh, styly but prob not corporate enough
- www.orvettagrove.com - spacious, beautiful, slightly dated tho
- www.plinzer.co.uk - ignore the colours. Like the simplicity, larger font size (although want to stick with sans-serif fonts for main content)

DELIVERABLES
The final designs should be delivered as one or more PSD files with clearly named layers. All design elements and treatments should be separated out, for example use adjustment layers rather than applied (and subsequently irreversible) adjustments, strokes, shading, etc.

WHAT NEXT
I'll be monitoring the contest every day and can respond to questions fast. You can IM me on Skype or MSN.

Reason: Hi folks,

I am extending the deadline to this project as I am travelling this week and therefore will not be able to make a final decision until next Monday. I will try and provide further feedback over the course of this week but I am only going to be online occasionally so be prepared to wait a few days for a reply from me.

Thanks for all the designs so far.

Owen

Target Market(s)

In order of importance, most important first

1. Potential customers - UK & US financial industry HR professionals, short on time. Heard about us already, want to find out more about what we do, confirm relevance for their needs. Core goal - establish credibility: are we properly resourced, will we be around for years to come, are we *real*.

2. Existing customers - UK & US financial industry professionals, short on time, under pressure, want results quickly, minimum faff, expect high quality, slickly presented information. Primary action: login and use surveys.

3. Industry professionals/researchers - probably arriving through blog content, looking to browse and hoover information. Valuable for their ability to spread awareness of who we are amongst their peers.

Industry/Entity Type

Financial

Requirements
Must have
• GENERAL
Style cues - Corporate, professional, financial, stylish, slick, clean, spacious, light
Size - standard 960px grid

NAVIGATION
- [ Home | About us | Surveys | Consulting | Blog ]
- Sub-nav (roll-over dropdown) on About Us, Surveys & Consulting

ALL PAGES
- Site navigation
- Client login (on screen permanently or link to ajaxy in-page pop-up)
- Footer section
- Existing logo (attached)* - this is obviously an important reference point in the design, esp colour

HOME PAGE
- Communicate (link thru to?) survey/consulting split
- Large photo(s)/backdrop (2-3 interchangeable options ideally). Please consider what rights agreement will be necessary for any photos you include in your design.
- Possibly bigger more prominent version of logo
- Strap line/sentence - "Focussed data is the key to success"
- 3 recent blog posts (should look good with and without blog post images)
- Free downloadable PDF research report + supporting blurb

INTERNAL PAGE
- Page title
- Content - typical page will be less than one screenfull
- Level 1 sub-heading
- Level 2 sub-heading
- Bulleted list
- Content supporting image (any image will do - interested in placement, borders (if any), spacing, caption, etc)
- 'Do something' button

* Note: there is some internal debate about this logo at the moment. Some (me) are keen for it to change, some (not me!) are not. If you have an web page design idea/concept that requires an evolution of the logo, go ahead and evolve it. We can explore this further in the design process as necessary, but don't sweat it.
Nice to have
• Values to communicate
- Knowledgeable
- Professional
- Secure
- Personal
- Experienced
- Financial industry specific
- Accurate
- Reliable
Should not have
• - Search box
- Social media links, other than RSS feed button (discrete)

```html
<!DOCTYPE html>
<html lang="en">
<head>
<meta charset="utf-8">
<title>Kelvane – Focussed data is the key to success</title>
<link rel="stylesheet" href="https://fonts.googleapis.com/css2?family=Tenor+Sans&family=Open+Sans:wght@400&family=Arimo:wght@400;700&display=swap">
<style>
  :root {
    --brand-red: #680a0a;
    --brand-red-light: #9c1c1c;
    --sky-top: #7db6dc;
    --sky-mid: #a9d0e8;
    --sky-low: #cfe3ee;
    --panel-edge: #a8d4ec;
    --panel-body: #9dcbe4;
    --tab-top: #8cc2e2;
    --tab-bottom: #5e9fcb;
    --nav-grey: #dcdcdc;
    --white: #ffffff;
    --ink: #333333;
    --rule: #b5b5b5;
  }
  * { box-sizing: border-box; margin: 0; padding: 0; }
  html, body { width: 1200px; height: 750px; overflow: hidden; background: var(--white); }
  .page { position: relative; width: 1200px; height: 750px; overflow: hidden; font-family: "Arimo", Arial, sans-serif; }

  .hero-backdrop {
    position: absolute; left: 0; top: 0; width: 1200px; height: 563px;
    background: linear-gradient(180deg, var(--sky-top) 0%, var(--sky-mid) 55%, var(--sky-low) 88%, #b9b2aa 100%);
  }

  .brand-name {
    position: absolute; font-family: "Tenor Sans", sans-serif;
    color: var(--brand-red); line-height: 1; white-space: nowrap;
  }
  .brand-name.in-header { left: 167px; top: 44px; font-size: 34px; }
  .brand-name.in-footer { left: 980px; top: 584px; font-size: 22px; }

  .main-nav { position: absolute; left: 168px; top: 321px; width: 119px; list-style: none; }
  .main-nav li {
    height: 36px; margin-bottom: 1.5px; background: var(--nav-grey);
    font-family: "Tenor Sans", sans-serif; font-size: 13.5px; color: var(--brand-red);
    padding-left: 19px; line-height: 36px; text-transform: uppercase; white-space: nowrap;
  }

  .strapline { position: absolute; left: 328px; top: 70px; font-family: "Tenor Sans", sans-serif; font-weight: 400; }
  .strapline-lead { display: block; font-size: 54px; color: var(--white); letter-spacing: 1px; line-height: 1.1; }
  .strapline-rest { display: block; font-size: 40px; color: var(--brand-red); letter-spacing: 2px; line-height: 0.95; }

  .offer-panel {
    position: absolute; left: 667px; top: 267px; width: 392px; height: 244px;
    background: var(--panel-edge); padding: 8px;
  }
  .offer-inner { position: relative; width: 100%; height: 100%; background: var(--panel-body); }
  .offer-tab {
    position: absolute; top: 0; height: 51px; color: var(--white);
    background: linear-gradient(180deg, var(--tab-top), var(--tab-bottom));
    padding: 9px 12px; font-family: "Tenor Sans", sans-serif;
  }
  .offer-tab.is-active { left: 0; width: 187px; }
  .offer-tab.is-next { left: 189px; width: 188px; opacity: .85; }
  .offer-tab-title { font-size: 16px; line-height: 1.1; }
  .offer-tab-sub { font-family: "Arimo", sans-serif; font-size: 11.5px; }
  .offer-tab svg { position: absolute; right: 12px; top: 20px; }
  .offer-copy {
    position: absolute; left: 13px; top: 64px; width: 360px; white-space: nowrap;
    font-family: "Open Sans", Verdana, sans-serif; font-size: 15px; line-height: 22.5px; color: var(--white);
  }
  .button-more {
    position: absolute; left: 13px; top: 182px; width: 113px; height: 32px;
    background: linear-gradient(180deg, var(--brand-red-light), var(--brand-red));
    color: var(--white); font-size: 14px; line-height: 32px; text-align: center; border-radius: 2px;
  }

  .footer-heading { font-size: 16px; color: var(--brand-red); font-weight: 400; margin-bottom: 6px; }
  .footer-col { position: absolute; top: 581px; font-size: 11.5px; line-height: 15px; color: var(--ink); }
  .blog-col { left: 168px; width: 252px; }
  .blog-list { list-style: none; }
  .blog-list li { position: relative; padding: 0 0 8px 11px; margin-bottom: 7px; border-bottom: 1px solid var(--rule); }
  .blog-list li:last-child { border-bottom: none; }
  .blog-list li::before {
    content: ""; position: absolute; left: 2px; top: 3px;
    border-left: 5px solid var(--brand-red); border-top: 4px solid transparent; border-bottom: 4px solid transparent;
  }
  .read-more { color: var(--brand-red); text-decoration: underline; font-size: 10px; }

  .download-col { left: 459px; width: 250px; }
  .download-col p { padding-left: 2px; }
  .download-button {
    position: absolute; left: 0; top: 101px; width: 246px; height: 47px; border-radius: 4px;
    background: linear-gradient(180deg, #9ccbe6, #6ea8cf); color: var(--white);
    font-size: 16.5px; font-weight: 700; line-height: 15px; padding: 9px 0 0 58px; text-transform: uppercase;
  }
  .pdf-tile { position: absolute; left: 5px; top: 5px; width: 40px; height: 37px; background: var(--brand-red-light); border: 2px solid #e6e6e6; border-radius: 2px; }

  .contact-col { left: 732px; width: 200px; }
  .contact-col address { font-style: normal; padding-left: 2px; }
  .contact-email { margin-top: 15px; padding-left: 2px; }
  .copyright { margin-top: 18px; font-size: 10px; color: var(--brand-red); padding-left: 2px; }
</style>
</head>
<body>
<div class="page">
  <div class="hero-backdrop" role="img" aria-label="Photograph of a red suspension bridge's cables against a blue sky above a city skyline"></div>

  <div class="brand-name in-header">Kelvane</div>

  <ul class="main-nav">
    <li>Home</li>
    <li>About us</li>
    <li>Surveys</li>
    <li>Consulting</li>
    <li>Blog</li>
  </ul>

  <h1 class="strapline">
    <span class="strapline-lead">FOCUSSED DATA</span>
    <span class="strapline-rest">is the key to success</span>
  </h1>

  <section class="offer-panel">
    <div class="offer-inner">
      <div class="offer-tab is-active">
        <div class="offer-tab-title">SURVEYS</div>
        <div class="offer-tab-sub">Aliquam erat volutpat.</div>
        <svg width="14" height="8" viewBox="0 0 14 8"><path d="M0 0h14L7 8z" fill="#fff"/></svg>
      </div>
      <div class="offer-tab is-next">
        <div class="offer-tab-title">CONSULTING</div>
        <div class="offer-tab-sub">Aliquam erat volutpat.</div>
        <svg width="8" height="16" viewBox="0 0 8 16" style="top:14px"><path d="M0 0l8 8-8 8z" fill="#fff"/></svg>
      </div>
      <p class="offer-copy">Lorem ipsum dolor sit amet, consectetur<br>adipiscing elit. Morbi a purus vel sem<br>accumsan varius eget ut erat. Class aptent<br>taciti sociosqu ad litora torquent per conubia<br>nostra, per inceptos himenaeos.</p>
      <div class="button-more">LEARN MORE</div>
    </div>
  </section>

  <section class="footer-col blog-col">
    <h2 class="footer-heading">BLOG</h2>
    <ul class="blog-list">
      <li>Lorem ipsum dolor sit amet, consectetur adipiscing elit. <span class="read-more">LEARN MORE</span></li>
      <li>Morbi a purus vel sem accumsan varius eget ut erat. <span class="read-more">LEARN MORE</span></li>
      <li>Class aptent taciti sociosqu ad litora torquent per conubia nostra. <span class="read-more">LEARN MORE</span></li>
    </ul>
  </section>

  <section class="footer-col download-col">
    <h2 class="footer-heading">FREE Download</h2>
    <p>er inceptos himenaeos. Pellentesque habitant morbi tristique senectus et netus et malesuada fames ac turpis egestas. Aliquam erat volutpat. Maecenas dapibus</p>
    <div class="download-button"><span class="pdf-tile"></span>Research report +<br>supporting blurb</div>
  </section>

  <section class="footer-col contact-col">
    <h2 class="footer-heading">Contact Us</h2>
    <address>Kelvane<br>Suite 200 - 480 Marlow Ave. S.E.<br>Cityname, State Name<br>USA</address>
    <p class="contact-email">E-mail: contact@kelvane.com</p>
    <p class="copyright">© 2011 Kelvane.com. All rights reserved</p>
  </section>

  <div class="brand-name in-footer">Kelvane</div>
</div>
</body>
</html>
```